Letterhead and envelope design

Using current logo and colours I would like to have a new design done for a stationary set to be printed.

The new files should include logo, web and email address as well as,mailing address and phone number

Dov Harmsby
Harmsby Construction Inc
Box 27 Site 18 RR5
Brennock QX
T4K 2B9
Cell : 403-555-2917
Email: dov@harmsbyconstruction.example
web: harmsbyconstruction.example

```html
<!DOCTYPE html>
<html lang="en">
<head>
<meta charset="utf-8">
<title>Harmsby Construction – Letterhead and Envelope</title>
<link href="https://fonts.googleapis.com/css2?family=Source+Sans+3:wght@400;600;700&display=swap" rel="stylesheet">
<style>
  :root {
    --navy: #0f1a29;
    --orange: #d7692a;
    --paper: #ffffff;
    --ink: #3a3a3a;
    --backdrop: #484848;
    --light: #ffffff;
  }
  * { box-sizing: border-box; margin: 0; padding: 0; }
  html, body { width: 960px; height: 1200px; overflow: hidden; }
  body {
    background: var(--backdrop);
    font-family: "Source Sans 3", sans-serif;
    position: relative;
  }
  .sheet { position: absolute; background: var(--paper); overflow: hidden; }
  .letterhead { left: 178px; top: 65px; width: 605px; height: 782px; }
  .envelope { left: 160px; top: 866px; width: 640px; height: 284px; }
  .header-shape { position: absolute; left: 0; top: 0; display: block; }

  .brand { position: absolute; display: flex; align-items: center; gap: 9px; }
  .brand-ring {
    width: 60px; height: 60px; border-radius: 50%;
    border: 1.5px solid var(--light);
  }
  .brand-name {
    color: var(--light); font-weight: 600; font-size: 10px;
    line-height: 1.2; letter-spacing: 0.3px;
  }
  .brand-name span { display: block; }
  .brand-name .first { font-size: 13.5px; }

  .address, .contact {
    position: absolute; color: var(--light);
    font-size: 9px; line-height: 11.8px;
  }
  .address .company { color: var(--orange); font-weight: 700; }
  .divider { position: absolute; width: 1px; background: var(--orange); }
  .contact li { list-style: none; display: flex; align-items: center; gap: 6px; }
  .contact svg { width: 8px; height: 8px; flex: none; }

  .letter-body {
    position: absolute; left: 51px; top: 240px; width: 502px;
    color: var(--ink); font-size: 11.2px; line-height: 14.2px;
  }
  .salutation { margin-bottom: 42px; }
  .letter-body p.para { text-align: justify; margin-bottom: 14px; }
  .letter-body p.para.first { text-indent: 36px; }

  .envelope-foot {
    position: absolute; left: 0; bottom: 0; width: 100%; height: 14px;
    background: var(--navy);
  }
</style>
</head>
<body>

<section class="sheet letterhead" aria-label="Letterhead">
  <svg class="header-shape" width="605" height="114" viewBox="0 0 605 114">
    <path d="M0 0H605V107Q302 69 0 107Z" fill="var(--navy)"/>
    <path d="M0 107Q302 69 605 107L605 113Q302 77 0 113Z" fill="var(--orange)"/>
  </svg>

  <div class="brand" style="left:50px; top:25px;">
    <div class="brand-ring"></div>
    <div class="brand-name"><span class="first">HARMSBY</span><span>CONSTRUCTION</span></div>
  </div>

  <div class="divider" style="left:283px; top:31px; height:48px;"></div>
  <div class="address" style="left:296px; top:31px;">
    <div class="company">Harmsby Construction Inc</div>
    <div>Box 27 Site 18 RR5</div>
    <div>Brennock QX</div>
    <div>T4K 2B9</div>
  </div>

  <div class="divider" style="left:408px; top:31px; height:48px;"></div>
  <ul class="contact" style="left:424px; top:31px;">
    <li>
      <svg viewBox="0 0 8 8"><rect x="1.2" y="0.3" width="5.6" height="7.4" rx="1" fill="var(--orange)"/><rect x="2.3" y="1.3" width="3.4" height="4.2" fill="var(--navy)"/></svg>
      403-555-2917
    </li>
    <li>
      <svg viewBox="0 0 8 8" fill="none" stroke="var(--orange)" stroke-width="0.8"><circle cx="4" cy="4" r="3.5"/><ellipse cx="4" cy="4" rx="1.5" ry="3.5"/><path d="M0.5 4H7.5"/></svg>
      dov@harmsbyconstruction.example
    </li>
    <li>
      <svg viewBox="0 0 8 8"><rect x="0.3" y="1.5" width="7.4" height="5.5" fill="var(--orange)"/><path d="M0.3 1.5L4 4.6L7.7 1.5" fill="none" stroke="var(--navy)" stroke-width="0.7"/></svg>
      harmsbyconstruction.example
    </li>
  </ul>

  <article class="letter-body">
    <p class="salutation">Dear Dr</p>
    <p class="para first">Lorem ipsum dolor sit amet, consectetur adipiscing elit. Integer eu odio mattis, pulvinar turpis quis, faucibus nisl. Proin feugiat, erat vitae cursus pharetra, enim est semper ligula, in malesuada orci nisi et diam. Etiam elementum metus ac fringilla vulputate. Etiam mattis ligula sed ante mollis bibendum. Orci varius natoque penatibus et magnis dis parturient montes, nascetur ridiculus mus.</p>
    <p class="para">Ut nibh augue, blandit ac orci ac, rutrum congue enim. Suspendisse gravida vulputate felis, quis interdum orci tincidunt quis. Praesent imperdiet maximus neque. Mauris ut dui enim. Nullam at efficitur elit. Donec ante ipsum, fermentum at lectus vel, blandit vulputate ante. Proin luctus suscipit diam id vestibulum. Morbi malesuada id mauris eget ullamcorper.</p>
    <p class="para">Donec varius orci purus, vitae aliquam libero volutpat id. Integer sed imperdiet libero. Aliquam accumsan, risus sit amet ornare consectetur, turpis felis dictum justo, non rhoncus mauris dui sed velit. Pellentesque habitant morbi tristique senectus et netus et malesuada fames ac turpis egestas. Pellentesque tincidunt vitae ligula nec imperdiet. Donec sed congue enim. Nullam elementum faucibus nulla nec vestibulum. Sed at tempor ligula. In quis vulputate nunc. Integer at gravida lacus, ac tristique risus. Sed at vulputate nulla.</p>
    <p class="para">Praesent blandit nunc eu efficitur commodo. In tempor nisi ex, vel venenatis ante vestibulum a. Duis vestibulum nibh a erat sagittis, nec euismod lorem varius. Nam ultricies turpis sed justo sollicitudin volutpat. Morbi sed mollis eros. Sed quis tortor id enim vehicula porttitor. Curabitur non aliquam ex. Phasellus dignissim fermentum elit, at finibus ligula mattis eget.</p>
  </article>
</section>

<section class="sheet envelope" aria-label="Envelope">
  <svg class="header-shape" width="640" height="123" viewBox="0 0 640 123">
    <path d="M0 0H640V111Q320 77 0 111Z" fill="var(--navy)"/>
    <path d="M0 111Q320 77 640 111L640 122Q320 84 0 122Z" fill="var(--orange)"/>
  </svg>

  <div class="brand" style="left:24px; top:24px;">
    <div class="brand-ring"></div>
    <div class="brand-name"><span class="first">HARMSBY</span><span>CONSTRUCTION</span></div>
  </div>

  <div class="address" style="left:502px; top:31px;">
    <div class="company">Harmsby Construction Inc</div>
    <div>Box 27 Site 18 RR5</div>
    <div>Brennock QX</div>
    <div>T4K 2B9</div>
  </div>

  <div class="envelope-foot"></div>
</section>

</body>
</html>
```